Label for a tea in a metal box

We need a label for a tea-metal box. The box will be made of silver aluminum. A photo of the metal box is attached. The metal box is together with an infuser (sieve) in a gift box. You can see this in the photo. The label should the dimensions 3.2 cm x 16 cm (total). The label passes through the entire box, is thus glued to the front side, passes over the cover and goes further to the rear and down. We need a coherent area, it is printed in a part. The surface will be split optically into three parts: front, top and back. Warning: The back of course, must be applied in the design rotated by 180 degrees. The top shows in the same direction as the front. The label is printed as a whole and bonded as a whole. This is also from the attached file "feature pattern" seen. In the box of loose Darjeeling Tea will be. The label should look very classy & premium, so minimalist, clean. Not too squashed, not too many different fonts and sizes, just clean, noble and premium. The design should communicate the following values: precious, premium, quality, quality. It should not look too old-fashioned, but also not very hip and trendy. It is indeed modern and vigorous look, but work has also for older customers. You are welcome to work with colors, but please simply, and tea fits as dark green, black, etc. Here is the text that you want on the label and other comments as well as the functional model and a view of the box.
Updates

Target Market(s)

Germany

Requirements
Must have
• The font size must be at least 0.9 mm (based on the small "x")

```html
<!DOCTYPE html>
<html lang="de">
<head>
<meta charset="utf-8">
<title>Darjeeling premium – Etikett</title>
<link href="https://fonts.googleapis.com/css2?family=Playfair+Display:wght@500;600&family=Raleway:wght@300;400&display=swap" rel="stylesheet">
<style>
  :root{
    --page:#ffffff;
    --tea-green:#6e7d4e;
    --band-green:#7c8a5d;
    --edge-cream:#e6e5c6;
    --ink-light:#eef0df;
    --ink-soft:#dfe4c8;
    --art-light:#8f9c72;
    --art-dark:#4d5639;
  }
  *{margin:0;padding:0;box-sizing:border-box}
  html,body{width:1200px;height:960px;overflow:hidden;background:var(--page)}
  .label{
    position:absolute;left:564px;top:24px;width:176px;height:922px;
    background:var(--tea-green);color:var(--ink-light);
    font-family:"Raleway",sans-serif;font-weight:300;
  }
  .edge{position:absolute;left:0;width:100%;height:8px;background:var(--edge-cream)}
  .edge--top{top:0}
  .edge--bottom{bottom:0;height:10px}
  .pattern-band{
    position:absolute;left:0;width:100%;height:23px;
    background:var(--band-green);
    border-top:1px solid var(--ink-soft);border-bottom:1px solid var(--ink-soft);
    opacity:.9;
  }
  .pattern-band--upper{top:260px}
  .pattern-band--lower{top:638px}

  /* back panel, printed upside down */
  .panel-back{
    position:absolute;left:0;top:8px;width:176px;height:252px;
    transform:rotate(180deg);
  }
  .panel-back .line{
    position:absolute;left:6px;font-size:9px;line-height:1;white-space:nowrap;letter-spacing:.1px;
  }
  .brew-icons{position:absolute;left:0;top:34px;width:176px;height:28px}
  .brew-values{position:absolute;top:64px;left:0;width:176px;font-size:10px;font-weight:400}
  .brew-values span{position:absolute;transform:translateX(-50%);white-space:nowrap}

  /* title blocks */
  .title-block{position:absolute;left:0;width:176px;text-align:center}
  .title-block .illustration{
    display:block;margin:0 auto;width:134px;height:68px;border-radius:40px 40px 6px 6px;
    background:radial-gradient(ellipse at 50% 60%,var(--art-dark) 0 22%,var(--art-light) 45%,var(--tea-green) 78%);
  }
  .title-block .product-name{
    font-family:"Playfair Display",serif;font-weight:600;font-size:36px;line-height:1;
    color:#fbfbf5;margin-top:-4px;letter-spacing:-.5px;
  }
  .title-block .product-grade{
    font-family:"Playfair Display",serif;font-weight:500;font-size:20px;line-height:.9;color:#fbfbf5;
    margin-left:30px;
  }
  .title-block .grade-code{font-size:12px;letter-spacing:.4px;margin-top:4px;color:var(--ink-soft)}
  .title-block--top{top:290px}
  .title-block--front{top:702px}
  .divider{display:block;margin:6px auto 4px}
  .tea-facts{font-size:7.5px;line-height:11.5px;letter-spacing:.2px;text-transform:uppercase;color:var(--ink-soft)}
</style>
</head>
<body>
<div class="label">
  <div class="edge edge--top"></div>

  <section class="panel-back">
    <svg class="brew-icons" viewBox="0 0 176 28" aria-hidden="true">
      <g fill="none" stroke="var(--ink-light)" stroke-width="1.3">
        <circle cx="33" cy="14" r="11"/>
        <line x1="33" y1="14" x2="38" y2="8"/>
        <rect x="91" y="3" width="6" height="20" rx="3"/>
        <line x1="94" y1="9" x2="94" y2="20"/>
        <path d="M134 16 a9 8 0 0 1 18 0 z" fill="var(--ink-light)"/>
        <line x1="152" y1="16" x2="172" y2="16"/>
      </g>
    </svg>
    <div class="brew-values">
      <span style="left:33px">2-3 Min.</span>
      <span style="left:94px">100 °C</span>
      <span style="left:148px">13 g/l</span>
    </div>
    <p class="line" style="top:88px">Für optimalen Geschmack</p>
    <p class="line" style="top:100px">weiches Wasser verwenden.</p>
    <p class="line" style="top:126px">Inhalt: 20 g</p>
    <p class="line" style="top:150px">Mindestens haltbar bis: 23. 08. 2018</p>
    <p class="line" style="top:165px">Charge: L02016/25702</p>
    <p class="line" style="top:192px">Exklusiv für die Grußkiste</p>
    <p class="line" style="top:204px">ausgewählt von Velden Tee GmbH</p>
    <p class="line" style="top:217px">Lindenweg 12, D-20000 Musterstadt</p>
  </section>

  <div class="pattern-band pattern-band--upper" role="img" aria-label="Schmales Zickzack-Ornamentband"></div>

  <section class="title-block title-block--top">
    <span class="illustration" role="img" aria-label="Illustration: Teekanne, Teeschale, Vogel und Blüten"></span>
    <h2 class="product-name">Darjeeling</h2>
    <p class="product-grade">premium</p>
    <p class="grade-code">FTGFOP 1</p>
  </section>

  <div class="pattern-band pattern-band--lower" role="img" aria-label="Schmales Zickzack-Ornamentband"></div>

  <section class="title-block title-block--front">
    <span class="illustration" role="img" aria-label="Illustration: Teekanne, Teeschale, Vogel und Blüten"></span>
    <h1 class="product-name">Darjeeling</h1>
    <p class="product-grade">premium</p>
    <p class="grade-code">FTGFOP 1</p>
    <svg class="divider" width="134" height="8" viewBox="0 0 134 8" aria-hidden="true">
      <g stroke="var(--ink-light)" stroke-width="1" fill="var(--ink-light)">
        <line x1="2" y1="4" x2="54" y2="4"/>
        <line x1="80" y1="4" x2="132" y2="4"/>
        <path d="M0 4 l6 -3 v6 z M134 4 l-6 -3 v6 z" stroke="none"/>
        <circle cx="58" cy="4" r=".8"/><circle cx="62" cy="4" r=".8"/><circle cx="67" cy="4" r=".8"/>
        <circle cx="72" cy="4" r=".8"/><circle cx="76" cy="4" r=".8"/>
      </g>
    </svg>
    <p class="tea-facts">100 % Schwarzer Tee<br>Hollin Farm im indischen Himalaya<br>Fein, aromatisch &amp; blumig</p>
  </section>

  <div class="edge edge--bottom"></div>
</div>
</body>
</html>
```